Business Card Design

Lintel Comms is a public relations consultancy service for the self build, home refurbishment and home improvement market.
It represents everything about 'home' so envisage logo featuring maybe roof pitch over the 'A' of Lintel. Colour/font undecided.

Industry/Entity Type

Home Improvement

Contact Information for Business Card

Fenella Coxworth
fenella@lintelcomms.co.uk
Telephone Direct: 0788 142 6597

```html
<!DOCTYPE html>
<html lang="en">
<head>
<meta charset="utf-8">
<title>Lintel Comms – Business Card</title>
<link rel="stylesheet" href="https://fonts.googleapis.com/css2?family=Arimo:wght@400;700&display=swap">
<style>
  :root {
    --page-bg: #e9e6e2;
    --card-base: #475866;
    --card-deep: #34475a;
    --text-light: #e4e7ea;
    --text-soft: #c9d0d6;
  }
  * { margin: 0; padding: 0; box-sizing: border-box; }
  html, body {
    width: 1200px;
    height: 720px;
    overflow: hidden;
    background: var(--page-bg);
    font-family: "Arimo", Arial, sans-serif;
  }
  .canvas {
    position: relative;
    width: 1200px;
    height: 720px;
  }
  .business-card {
    position: absolute;
    left: 120px;
    top: 80px;
    width: 960px;
    height: 560px;
    overflow: hidden;
    box-shadow: 0 10px 30px rgba(0, 0, 0, 0.18);
  }
  .floorplan-backdrop {
    position: absolute;
    inset: 0;
    background: linear-gradient(160deg, var(--card-base) 0%, var(--card-base) 55%, var(--card-deep) 100%);
  }
  .brand-mark {
    position: absolute;
    left: 70px;
    top: 190px;
    display: flex;
    align-items: center;
    gap: 16px;
    color: var(--text-light);
    font-weight: 700;
    font-size: 56px;
    line-height: 1;
  }
  .brand-mark .mark-square {
    width: 40px;
    height: 40px;
    background: var(--text-light);
  }
  .company-name {
    position: absolute;
    left: 380px;
    top: 170px;
    font-weight: 700;
    font-size: 30px;
    color: var(--text-light);
    white-space: nowrap;
  }
  .person {
    position: absolute;
    left: 500px;
    top: 240px;
    text-align: right;
  }
  .person-name {
    font-weight: 700;
    font-size: 28px;
    color: var(--text-soft);
  }
  .person-note {
    font-weight: 400;
    font-size: 20px;
    color: var(--text-soft);
    margin-top: 4px;
  }
  .contact {
    position: absolute;
    left: 90px;
    top: 420px;
    font-size: 23px;
    color: var(--text-light);
    line-height: 1.6;
  }
  .contact-label {
    display: inline-block;
    width: 92px;
    font-weight: 700;
    color: var(--text-soft);
  }
</style>
</head>
<body>
  <main class="canvas">
    <section class="business-card">
      <div class="floorplan-backdrop" role="img" aria-label="Faint architectural floor plan pattern in slate blue tones"></div>

      <div class="brand-mark">
        <span class="mark-square"></span>
        <span class="mark-name">Lintel</span>
      </div>

      <h1 class="company-name">Lintel Comms Home Improvement</h1>

      <div class="person">
        <p class="person-name">Fenella Coxworth</p>
        <p class="person-note">Fully Insured</p>
      </div>

      <div class="contact">
        <p><span class="contact-label">Phone:</span>0788 142 6597</p>
        <p><span class="contact-label">Email:</span>fenella@lintelcomms.co.uk</p>
      </div>
    </section>
  </main>
</body>
</html>
```